Property management company looking for modern card design

We at Blue Heron Partners provides property management services for its residential and commercial properties, with expertise in all categories of multifamily, industrial and office projects throughout California.

We need a business card design that is professional and modern designed business card. In our field, clients get hundreds of business cards, we would like our card to stand out.

Please avoid small print.

Target Market(s)

Professionals and high end clients

Industry/Entity Type

Financial Planning

Contact Information for Business Card

Company Name: Blue Heron Partners, Name, email, license #, phone number, website blueheronpartners.com

Font styles to use
Sans Serif

Requirements
Must have
• The card design needs to be adaptable because there is a possibly we will be expanding into different sectors other than real estate. The card design should be focused on financial planning and asset management.
Nice to have
• Modern and simple business card. Eye catching. Non-standard size/shaped cards would be great.
• blueheronpartners.com
Should not have
• Too many bright color or any pictures or shapes of real estate stuff.

```html
<!DOCTYPE html>
<html lang="en">
<head>
<meta charset="utf-8">
<title>Blue Heron Partners – Business Card</title>
<link rel="stylesheet" href="https://fonts.googleapis.com/css2?family=Montserrat:wght@400;500;700&display=swap">
<style>
  :root {
    --bg: #ecebe8;
    --card-dark: #333333;
    --card-light: #ffffff;
    --brand-red: #c93232;
    --ink: #2b2b2b;
    --ink-soft: #3a3a3a;
  }
  * { margin: 0; padding: 0; box-sizing: border-box; }
  html, body {
    width: 1200px; height: 1000px; overflow: hidden;
    background: var(--bg);
    font-family: "Montserrat", Arial, sans-serif;
  }
  .canvas { position: relative; width: 1200px; height: 1000px; }
  .card {
    position: absolute; left: 288px; width: 626px; height: 358px;
    border-radius: 28px;
    box-shadow: 0 6px 14px rgba(0,0,0,0.25);
    overflow: hidden;
  }
  .card--front { top: 140px; background: var(--card-dark); }
  .card--back { top: 532px; background: var(--card-light); }

  .front-mark__dot {
    position: absolute; left: 223px; top: 90px;
    width: 180px; height: 180px; border-radius: 50%;
    background: var(--brand-red);
  }
  .front-mark__name {
    position: absolute; left: 0; right: 0; top: 290px;
    text-align: center;
    color: var(--card-light); font-size: 17px; font-weight: 500;
    letter-spacing: 2px; text-transform: uppercase;
  }

  .holder { position: absolute; left: 34px; top: 38px; }
  .holder__bar {
    position: absolute; left: -34px; top: 4px;
    width: 8px; height: 34px; background: var(--brand-red);
  }
  .holder__name { color: var(--brand-red); font-size: 22px; font-weight: 700; line-height: 1.1; }
  .holder__title { color: var(--ink-soft); font-size: 15px; font-weight: 400; margin-top: 2px; }

  .wordmark {
    position: absolute; right: 36px; top: 44px;
    color: var(--ink); font-size: 22px; font-weight: 400;
    letter-spacing: 1px; text-transform: uppercase;
  }

  .details { position: absolute; left: 36px; top: 222px; color: var(--ink-soft); font-size: 15px; }
  .details__license { margin-bottom: 12px; line-height: 20px; }
  .details__license span { color: var(--brand-red); }
  .contact { list-style: none; }
  .contact li { display: flex; align-items: center; gap: 8px; height: 23px; }
  .contact svg { width: 13px; height: 13px; flex: none; }
</style>
</head>
<body>
<main class="canvas">
  <section class="card card--front" aria-label="Card front">
    <div class="front-mark__dot"></div>
    <div class="front-mark__name">Blue Heron Partners</div>
  </section>

  <section class="card card--back" aria-label="Card back">
    <div class="holder">
      <div class="holder__bar"></div>
      <div class="holder__name">Daniel Reyes</div>
      <div class="holder__title">President</div>
    </div>

    <div class="wordmark">Blue Heron Partners</div>

    <div class="details">
      <p class="details__license"><span>License</span>: #7390418</p>
      <ul class="contact">
        <li>
          <svg viewBox="0 0 16 16" aria-hidden="true"><path fill="#c93232" d="M4 1l2.5 3-1.6 1.6a9 9 0 0 0 5.5 5.5L12 9.5l3 2.5-1.5 2.5C8 15 1 8 1.5 2.5z"/></svg>
          555-3190-2746
        </li>
        <li>
          <svg viewBox="0 0 16 16" aria-hidden="true"><rect x="1" y="3" width="14" height="10" fill="#c93232"/><path d="M1 3l7 6 7-6" stroke="#fff" stroke-width="1.4" fill="none"/></svg>
          info@blueheronpartners.com
        </li>
        <li>
          <svg viewBox="0 0 16 16" aria-hidden="true" fill="none" stroke="#c93232" stroke-width="1.4"><circle cx="8" cy="8" r="6.5"/><ellipse cx="8" cy="8" rx="3" ry="6.5"/><path d="M1.5 8h13"/></svg>
          www.blueheronpartners.com
        </li>
      </ul>
    </div>
  </section>
</main>
</body>
</html>
```